Tess Marlowe Communication business card

I am starting a small, country-based business that offers writing, communication and marketing services to a wide range of clients, inner city big business, to mining, through to agriculture.

The appeal of my business is that it's mobile and flexible. It's just me, with lots of hands-on experience on construction and infrastructure projects.

I can provide the following services:

• Communication planning and management
• Issues and media management
• Marketing and communication materials
• Project management and strategy
• Government liaison
• Incident management communication
• Stakeholder management

It would be great to be able to use the elements of the business card design on other stationery.

Industry/Entity Type

Communication

Requirements
Must have
• The following information:

Tess Marlowe
M: 0427 391 864
E: tess@tmcommsmail.com

PO Box 152
Durrandale Q 4472
Nice to have
• a rural element (windmill, workboots, wheat stalk)

```html
<!DOCTYPE html>
<html lang="en">
<head>
<meta charset="utf-8">
<title>Tess Marlowe Communication – Stationery</title>
<link href="https://fonts.googleapis.com/css2?family=PT+Sans:ital,wght@0,400;0,700;1,400;1,700&family=Courgette&display=swap" rel="stylesheet">
<style>
  :root {
    --red: #c8101a;
    --red-dark: #8e0a10;
    --red-light: #e4232b;
    --ink: #1a1a1a;
    --grey-text: #444;
    --paper: #ffffff;
    --paper-grey: #e9e9e9;
    --stage-dark: #050505;
    --stage-glow: #5a5a5a;
    --faint: rgba(200, 16, 26, 0.10);
  }
  * { margin: 0; padding: 0; box-sizing: border-box; }
  html, body { width: 1200px; height: 871px; overflow: hidden; background: var(--stage-dark); }
  .board {
    position: relative; width: 1200px; height: 871px; overflow: hidden;
    font-family: "PT Sans", Arial, sans-serif; color: var(--ink);
    background: radial-gradient(ellipse 520px 360px at 840px 190px, var(--stage-glow) 0%, #1c1c1c 55%, var(--stage-dark) 100%);
  }
  .masthead {
    position: absolute; left: 0; top: 0; width: 1200px; height: 174px;
    background: var(--paper); display: flex; align-items: center; justify-content: center; gap: 14px;
  }
  .brand-dot { border-radius: 50%; background: var(--red); flex: none; }
  .brand-name { font-weight: 700; color: var(--red); white-space: nowrap; letter-spacing: 0.5px; }
  .masthead .brand-dot { width: 46px; height: 46px; }
  .masthead .brand-name { font-size: 34px; }

  .faint-mark { position: absolute; border-radius: 50%; background: var(--faint); }

  /* Letterhead */
  .letterhead {
    position: absolute; left: 15px; top: 297px; width: 368px; height: 518px;
    background: var(--paper); overflow: hidden;
    box-shadow: 0 2px 10px rgba(0,0,0,0.5);
  }
  .letterhead .brand { position: absolute; left: 16px; top: 26px; display: flex; align-items: center; gap: 6px; }
  .letterhead .brand-dot { width: 14px; height: 14px; }
  .letterhead .brand-name { font-size: 11px; }
  .contact { font-size: 8.5px; font-weight: 700; font-style: italic; line-height: 1.35; }
  .contact dl { display: grid; grid-template-columns: auto auto; column-gap: 4px; }
  .contact dt { letter-spacing: 1px; }
  .contact dd { font-weight: 400; }
  .letterhead .contact { position: absolute; left: 207px; top: 12px; }
  .letterhead .swoosh { position: absolute; left: 0; bottom: 0; width: 368px; height: 64px; }

  /* Business cards */
  .card { position: absolute; width: 328px; height: 187px; border-radius: 9px; overflow: hidden; box-shadow: 0 4px 14px rgba(0,0,0,0.55); }
  .card-back { left: 792px; top: 227px; background: linear-gradient(135deg, #ffffff 0%, #d9d9d9 100%); }
  .card-back .services {
    position: absolute; left: 49px; top: 30px; list-style: none;
    font-size: 11.6px; font-style: italic; line-height: 16.8px; color: var(--ink);
  }
  .card-back .services li::before { content: "•"; margin-right: 6px; font-style: normal; }
  .card-art { position: absolute; left: 0; top: 0; width: 100%; height: 100%; }

  .card-front { left: 503px; top: 334px; background: linear-gradient(180deg, #ffffff 0%, #d6d6d6 100%); }
  .card-front .brand { position: absolute; left: 20px; top: 20px; display: flex; align-items: center; gap: 6px; }
  .card-front .brand-dot { width: 15px; height: 15px; }
  .card-front .brand-name { font-size: 12px; line-height: 15px; }
  .card-front .holder {
    position: absolute; right: 30px; top: 90px; color: var(--paper);
    font-size: 11px; letter-spacing: 1.5px; text-transform: uppercase;
  }
  .card-front .contact { position: absolute; left: 22px; top: 106px; color: var(--paper); font-size: 8.5px; }

  /* Envelopes */
  .envelope { position: absolute; width: 316px; height: 139px; box-shadow: 0 3px 10px rgba(0,0,0,0.5); overflow: hidden; }
  .envelope-back { left: 506px; top: 596px; background: linear-gradient(180deg, #f4f4f4, #cfcfcf); }
  .envelope-front { left: 467px; top: 692px; background: linear-gradient(135deg, #ffffff 0%, #cdcdcd 100%); border: 1px solid #333; }

  /* Thank-you cards */
  .thanks { position: absolute; top: 600px; width: 118px; height: 119px; background: linear-gradient(135deg, #ffffff, #dedede); overflow: hidden; box-shadow: 0 2px 8px rgba(0,0,0,0.5); }
  .thanks-left { left: 900px; }
  .thanks-right { left: 1024px; }
  .thanks .band {
    position: absolute; left: 0; bottom: 6px; width: 100%; height: 13px;
    background: linear-gradient(90deg, var(--red-dark), var(--red-light));
    color: var(--paper); font-family: "Courgette", cursive; font-size: 8.5px; line-height: 13px; padding-left: 8px;
  }
</style>
</head>
<body>
<main class="board">

  <header class="masthead">
    <span class="brand-dot"></span>
    <span class="brand-name">Tess Marlowe Communication</span>
  </header>

  <section class="letterhead" aria-label="Letterhead">
    <div class="brand"><span class="brand-dot"></span><span class="brand-name">Tess Marlowe Communication</span></div>
    <div class="contact">
      <dl>
        <dt>Address -</dt><dd>PO Box 152<br>Durrandale Q 4472</dd>
        <dt>Mobile</dt><dd>- 0427 391 864</dd>
        <dt>Email</dt><dd>- tess@tmcommsmail.com</dd>
      </dl>
    </div>
    <span class="faint-mark" style="left:208px; top:350px; width:104px; height:104px;"></span>
    <svg class="swoosh" viewBox="0 0 368 64" preserveAspectRatio="none">
      <defs>
        <linearGradient id="lhRed" x1="0" y1="0" x2="1" y2="0">
          <stop offset="0" stop-color="#8e0a10"/><stop offset="0.5" stop-color="#d4121c"/><stop offset="1" stop-color="#e4232b"/>
        </linearGradient>
      </defs>
      <path d="M0,6 C110,2 230,30 300,64 L0,64 Z" fill="url(#lhRed)"/>
      <path d="M0,18 C120,16 220,40 270,64" fill="none" stroke="#fff" stroke-width="3"/>
    </svg>
  </section>

  <section class="card card-back" aria-label="Business card, back">
    <svg class="card-art" viewBox="0 0 328 187" preserveAspectRatio="none">
      <defs>
        <linearGradient id="backRed" x1="0" y1="0" x2="1" y2="0">
          <stop offset="0" stop-color="#e4232b"/><stop offset="1" stop-color="#8e0a10"/>
        </linearGradient>
      </defs>
      <path d="M40,187 C150,170 250,150 328,120 L328,187 Z" fill="url(#backRed)"/>
    </svg>
    <ul class="services">
      <li>Communication planning and management</li>
      <li>Issues and media management</li>
      <li>Marketing and communication materials</li>
      <li>Project management and strategy</li>
      <li>Government liaison</li>
      <li>Incident management communication</li>
      <li>Stakeholder management</li>
    </ul>
  </section>

  <section class="card card-front" aria-label="Business card, front">
    <svg class="card-art" viewBox="0 0 328 187" preserveAspectRatio="none">
      <defs>
        <linearGradient id="frontRed" x1="0" y1="0" x2="0" y2="1">
          <stop offset="0" stop-color="#d4121c"/><stop offset="1" stop-color="#8e0a10"/>
        </linearGradient>
      </defs>
      <path d="M0,74 C120,72 250,56 328,30 L328,158 C220,168 110,158 0,184 Z" fill="url(#frontRed)"/>
      <path d="M0,81 C120,79 250,63 328,37" fill="none" stroke="#ffffff" stroke-width="2"/>
    </svg>
    <div class="brand"><span class="brand-dot"></span><span class="brand-name">Tess Marlowe Communication</span></div>
    <div class="holder">Tess Marlowe</div>
    <div class="contact">
      <dl>
        <dt>Address -</dt><dd>PO Box 152<br>Durrandale Q 4472</dd>
        <dt>Mobile</dt><dd>- 0427 391 864</dd>
        <dt>Email</dt><dd>- tess@tmcommsmail.com</dd>
      </dl>
    </div>
  </section>

  <section class="envelope envelope-back" aria-label="Envelope, back">
    <svg class="card-art" viewBox="0 0 316 139" preserveAspectRatio="none">
      <defs>
        <radialGradient id="flapRed" cx="0.5" cy="0.3" r="0.7">
          <stop offset="0" stop-color="#e4232b"/><stop offset="1" stop-color="#8e0a10"/>
        </radialGradient>
      </defs>
      <path d="M0,0 L316,0 L316,10 L158,56 L0,10 Z" fill="url(#flapRed)"/>
    </svg>
  </section>

  <section class="envelope envelope-front" aria-label="Envelope, front">
    <span class="faint-mark" style="left:104px; top:36px; width:88px; height:88px;"></span>
  </section>

  <section class="thanks thanks-left" aria-label="Thank-you card">
    <span class="faint-mark" style="left:34px; top:20px; width:58px; height:58px;"></span>
    <div class="band">Thank You !</div>
  </section>
  <section class="thanks thanks-right" aria-label="Thank-you card">
    <span class="faint-mark" style="left:34px; top:20px; width:58px; height:58px;"></span>
    <div class="band">Thank You !</div>
  </section>

</main>
</body>
</html>
```